A Speech Therapy Business needs to update their logo

I need an update to the font and color of my logo to look more appealing. I am looking to open a private practice as a Speech Language Pathologist that caters to adults and children. It needs to be sophisticated and friendly at the same time. I want to keep the silhouette in my logo as is, just update the font and color for "Brightpaths".
Industry/Entity Type
Business
Contact Information for Business Card
I want the business card to have my logo, my name (Dorota Valk, CCC-SLP, TSSLD) and that I am a Bilingual Speech Language Pathologist. Also, include my phone number, (555) 271-8390. Include my website, Brightpathsslp.example, and email address, dorotavalk@brightpathsslp.example
Look and feel
Each slider illustrates characteristics of the customer's brand and the style your logo design should communicate.

```html
<!DOCTYPE html>
<html lang="en">
<head>
<meta charset="utf-8">
<title>Brightpaths Business Card</title>
<link href="https://fonts.googleapis.com/css2?family=Lato:wght@400;700;900&display=swap" rel="stylesheet">
<style>
  :root {
    --page-bg: #e6e7e9;
    --card-white: #ffffff;
    --band-grey: #5f5f5f;
    --ink-grey: #5a5a5a;
    --text-light: #ffffff;
    --text-soft: #e9e9e9;
    --divider: #d8d8d8;
  }
  html, body {
    margin: 0;
    width: 1200px;
    height: 1200px;
    overflow: hidden;
    background: var(--page-bg);
    font-family: "Lato", sans-serif;
  }
  .canvas {
    width: 1200px;
    height: 1200px;
    display: flex;
    align-items: center;
    justify-content: center;
  }
  .business-card {
    position: relative;
    width: 1000px;
    height: 572px;
    background: var(--card-white);
    box-shadow: 0 6px 24px rgba(0,0,0,0.12);
    overflow: hidden;
  }
  .brand {
    position: absolute;
    left: 0;
    right: 0;
    top: 70px;
    display: flex;
    flex-direction: column;
    align-items: center;
  }
  .brand-silhouette {
    width: 470px;
    height: 120px;
    border-radius: 6px;
    background: linear-gradient(90deg, #6a6a6a, #8a8a8a);
  }
  .brand-name {
    margin-top: 14px;
    font-weight: 900;
    font-size: 64px;
    letter-spacing: 2px;
    color: var(--ink-grey);
    line-height: 1;
  }
  .info-band {
    position: absolute;
    left: 0;
    right: 0;
    top: 300px;
    bottom: 0;
    background: var(--band-grey);
    display: flex;
    align-items: center;
    justify-content: center;
    padding-bottom: 40px;
    box-sizing: border-box;
  }
  .person {
    text-align: right;
    color: var(--text-light);
    padding-right: 34px;
  }
  .person-name {
    font-weight: 700;
    font-size: 40px;
    line-height: 1.15;
  }
  .person-credentials {
    font-size: 27px;
    font-weight: 700;
  }
  .person-title {
    font-size: 29px;
    font-weight: 400;
    color: var(--text-soft);
    line-height: 1.2;
  }
  .divider {
    width: 2px;
    height: 150px;
    background: var(--divider);
  }
  .contacts {
    list-style: none;
    margin: 0;
    padding: 0 0 0 28px;
    color: var(--text-soft);
    font-size: 27px;
  }
  .contacts li {
    display: flex;
    align-items: center;
    gap: 18px;
    line-height: 1.55;
  }
  .contacts svg {
    width: 26px;
    height: 26px;
    flex: none;
  }
</style>
</head>
<body>
<main class="canvas">
  <section class="business-card">
    <div class="brand">
      <div class="brand-silhouette" role="img" aria-label="Silhouette of a row of people, adults to toddler, holding hands"></div>
      <div class="brand-name">BRIGHTPATHS</div>
    </div>
    <div class="info-band">
      <div class="person">
        <div class="person-name">Dorota Valk, <span class="person-credentials">CCC-SLP, TSSLD</span></div>
        <div class="person-title">Bilingual Speech Language<br>Pathologist</div>
      </div>
      <div class="divider"></div>
      <ul class="contacts">
        <li>
          <svg viewBox="0 0 24 24" aria-hidden="true"><path d="M7 3c-2 1-3 3-3 6 0 6 5 12 11 12 2 0 3-1 4-2l-3-4-2 1c-2-1-4-4-5-6l1-2z" fill="#fff"/></svg>
          (555) 271-8390
        </li>
        <li>
          <svg viewBox="0 0 24 24" aria-hidden="true"><rect x="2" y="5" width="20" height="14" fill="none" stroke="#fff" stroke-width="2"/><path d="M2 5l10 8 10-8" fill="none" stroke="#fff" stroke-width="2"/></svg>
          dorotavalk@brightpathsslp.example
        </li>
        <li>
          <svg viewBox="0 0 24 24" aria-hidden="true"><g fill="none" stroke="#fff" stroke-width="1.6"><circle cx="12" cy="12" r="10"/><ellipse cx="12" cy="12" rx="4.5" ry="10"/><path d="M2 12h20M4 7h16M4 17h16"/></g></svg>
          Brightpathsslp.example
        </li>
      </ul>
    </div>
  </section>
</main>
</body>
</html>
```